Design a fun and engaging Social Media eBook

Graphic design job:

For initial concept stage, please provide some sample powerpoint designs of:
-A cover
-Section divides
-A few copy pages

We can then work on the full document which would be redesigning 22 pages of existing copy in word docs into the template.

Will be used to educate staff on Social Media.
We would like the design of the document to reflect the digital and social landscape. It should be fun and engaing.

Should demonstrate creativity, have social community focus, and be colourful and modern.

The audience is older people that need to be convinced about the benefits of social media and require some education / tips on how to use it. 40-60 year olds.

To be supplied to us in powerpoint.

Reason: This project has been extended, we have changed the category to graphic design and simplified the initial concept phase for designers to submit ideas.

Target Market(s)

Older staff that need to get the benefits of social media

Industry/Entity Type

Education

Requirements
Must have
• Must be supplied in Powerpoint.
Look modern, slick, cool, edgy

Look very "Tindro" brand in simplicity and digital sense.
Reflect a 'digital' type of design

Combine all documents into one clean document / workbook.

(Don't worry will not be ised for powerpoint presentations, just want it in an edible document format - so lots of text on a slide is fine) Finished product will be a PDF
Nice to have
• Interactive in some way with click throughs or page turners

```html
<!DOCTYPE html>
<html lang="en">
<head>
<meta charset="utf-8">
<title>Social Media Overview</title>
<link rel="stylesheet" href="https://fonts.googleapis.com/css2?family=Source+Sans+3:wght@400;600&display=swap">
<style>
  :root {
    --paper: #e6e7e8;
    --glow: #ffffff;
    --ink: #2e3134;
    --ink-soft: #6b6e71;
    --blue: #1e6fd0;
    --sky: #4fb3e8;
    --orange: #f5a316;
    --red: #e3262a;
    --grey: #a6a8ab;
  }
  html, body {
    margin: 0;
    padding: 0;
    overflow: hidden;
  }
  .cover {
    position: relative;
    width: 1200px;
    height: 900px;
    overflow: hidden;
    background:
      radial-gradient(ellipse 520px 440px at 470px 360px, var(--glow) 0%, rgba(255,255,255,0.55) 55%, rgba(255,255,255,0) 100%),
      var(--paper);
    font-family: "Source Sans 3", "Myriad Pro", sans-serif;
  }
  .cover__cluster {
    position: absolute;
    left: 120px;
    top: 50px;
    width: 740px;
    height: 620px;
  }
  .cover__title {
    position: absolute;
    left: 653px;
    top: 640px;
    margin: 0;
    font-size: 86px;
    font-weight: 600;
    line-height: 76px;
    letter-spacing: -1.5px;
    color: var(--ink);
    text-shadow: 0 2px 0 rgba(255,255,255,0.9);
  }
  .cover__subtitle {
    position: absolute;
    left: 657px;
    top: 806px;
    margin: 0;
    font-size: 31px;
    font-weight: 400;
    line-height: 1;
    color: var(--ink-soft);
    text-shadow: 0 1px 0 rgba(255,255,255,0.9);
  }
</style>
</head>
<body>
  <main class="cover">
    <svg class="cover__cluster" viewBox="0 0 740 620" role="img"
         aria-label="Speech-bubble shaped cluster of colourful social and communication icons: chat bubbles, envelopes, birds, stars, music notes, location pins, people and links">
      <defs>
        <linearGradient id="clusterTone" x1="0" y1="0" x2="1" y2="1">
          <stop offset="0" stop-color="var(--red)" stop-opacity="0.55"/>
          <stop offset="0.35" stop-color="var(--blue)" stop-opacity="0.5"/>
          <stop offset="0.65" stop-color="var(--orange)" stop-opacity="0.5"/>
          <stop offset="1" stop-color="var(--grey)" stop-opacity="0.45"/>
        </linearGradient>
      </defs>
      <path fill="url(#clusterTone)"
            d="M360 20 C560 20 730 110 730 260 C730 400 610 470 470 480
               C500 520 515 560 525 600 C480 560 440 520 400 495
               C200 500 20 420 20 270 C20 120 170 20 360 20 Z"/>
    </svg>

    <h1 class="cover__title">Social Media<br>Overview</h1>
    <p class="cover__subtitle">for Kestrel advisers</p>
  </main>
</body>
</html>
```